Willowmere Accord Business Card

Need a business card for my nonprofit, Willowmere Accord Inc. Willowmere Accord is a conflict resolution practice that offers services that help people resolve problems peacefully.

Got Conflict? Try Conflict Coaching. Initial consultation is complimentary

Marissa Dovrell-Kantz, PhD
Willowmere Accord Inc.
www.willowmereaccord.org
E: info@willowmereaccord.org
P: 555-318-4702

Would like the attached logo on it, as well as our slogan, which is Bringing Peace to the TableĀ®

```html
<!DOCTYPE html>
<html lang="en">
<head>
<meta charset="utf-8">
<title>Willowmere Accord – Business Card</title>
<link rel="stylesheet" href="https://fonts.googleapis.com/css2?family=Krona+One&family=Michroma&display=swap">
<style>
  :root {
    --ink: #231f20;
    --red: #bf2a26;
    --gold: #b08d32;
    --white: #ffffff;
    --page: #ffffff;
  }
  html, body {
    margin: 0;
    width: 1200px;
    height: 1200px;
    overflow: hidden;
    background: var(--page);
  }
  .card {
    position: absolute;
    left: 189px;
    width: 823px;
    height: 470px;
    overflow: hidden;
  }
  .card--front { top: 62px; }
  .card--back { top: 666px; }
  .card__shapes {
    position: absolute;
    inset: 0;
    width: 100%;
    height: 100%;
  }
  .wordmark {
    position: absolute;
    margin: 0;
    font-family: "Michroma", sans-serif;
    font-weight: 400;
    text-align: center;
    text-transform: uppercase;
    line-height: 1.45;
    white-space: nowrap;
    transform: translateX(-50%);
  }
  .card--front .wordmark {
    left: 304px;
    top: 142px;
    font-size: 35px;
    letter-spacing: 2px;
    color: var(--white);
  }
  .card--back .wordmark {
    left: 427px;
    top: 88px;
    font-size: 40px;
    letter-spacing: 3px;
    color: var(--gold);
  }
  .holder {
    position: absolute;
    left: 670px;
    top: 24px;
    transform: translateX(-50%);
    text-align: center;
    color: var(--white);
    white-space: nowrap;
  }
  .holder__name {
    margin: 0;
    font-family: "Krona One", sans-serif;
    font-size: 24px;
    line-height: 1.2;
  }
  .holder__title {
    margin: 2px 0 0;
    font-family: "Krona One", sans-serif;
    font-size: 15px;
    letter-spacing: 0.5px;
    text-transform: uppercase;
  }
  .contact {
    position: absolute;
    left: 573px;
    top: 240px;
    margin: 0;
    padding: 0;
    list-style: none;
    font-family: "Michroma", sans-serif;
    font-size: 7.5px;
    letter-spacing: 0.8px;
    line-height: 18px;
    text-transform: uppercase;
    color: var(--white);
    white-space: nowrap;
  }
  .web {
    position: absolute;
    left: 0;
    right: 0;
    top: 398px;
    margin: 0;
    text-align: center;
    font-family: "Michroma", sans-serif;
    font-size: 25px;
    letter-spacing: 6px;
    text-transform: uppercase;
    color: var(--white);
    white-space: nowrap;
  }
</style>
</head>
<body>

<section class="card card--front" aria-label="Business card front">
  <svg class="card__shapes" viewBox="0 0 1029 588" preserveAspectRatio="none" aria-hidden="true">
    <rect width="1029" height="588" fill="var(--ink)"/>
    <rect x="632" y="0" width="397" height="588" fill="var(--red)"/>
    <path d="M628,96 L632,96 C672,108 696,140 696,190 L696,430 C696,475 672,505 632,516 L628,516 Z" fill="var(--ink)"/>
    <path d="M0,88 C38,90 54,140 54,210 L54,390 C54,465 38,516 0,518 Z" fill="var(--red)"/>
  </svg>

  <p class="wordmark">Willowmere<br>Accord</p>

  <div class="holder">
    <p class="holder__name">Marissa Dovrell</p>
    <p class="holder__title">Kantz, PhD</p>
  </div>

  <ul class="contact">
    <li>P: 555-318-4702</li>
    <li>E: info@willowmereaccord.org</li>
    <li>www.willowmereaccord.org</li>
  </ul>
</section>

<section class="card card--back" aria-label="Business card back">
  <svg class="card__shapes" viewBox="0 0 1029 588" preserveAspectRatio="none" aria-hidden="true">
    <rect width="1029" height="588" fill="var(--ink)"/>
    <rect x="0" y="404" width="1029" height="184" fill="var(--red)"/>
    <path d="M257,400 L257,418 C257,444 280,459 315,459 L758,459 C793,459 816,444 816,418 L816,400 Z" fill="var(--ink)"/>
  </svg>

  <p class="wordmark">Willowmere<br>Accord</p>

  <p class="web">www.willowmereaccord.org</p>
</section>

</body>
</html>
```